GO SMOKY - BBQ Sauce Bottle Packaging

We are a BBQ&Grill restaurant. We are ready to launch our sauce line commercially. We have selected a boston round plastic bottle that will have a twist top. We have 3 flavors. The main design would be used for each flavor.

"K" sauce- Kansas - sweet with a little heat
"T" sauce - Texas - tangy and spicy
"C" sauce- Carolina - mustard based
16 oz bottle
Right side of design should have "our story"
Left side will be ingredients, crafted in small batches,
It should Incorporate our logo shape and other elements such as orange star. Attached are the design specs, the bottle that will be used, examples of some of our currently used marketing pieces (menu, billboard), and other design ideas. Our website is www.thewillowcrestbbq.com

Target Market(s)

25-50 grocery shoppers, texas bbq seekers, condiments

Industry/Entity Type

Restaurant

Font styles to use
Serif

Requirements
Must have
• Shelf appeal
• http://www.vesselandwrapsupply.com/item/Q813
• Label specs
Nice to have
• Distressed look
• Colors are
• CMYK 94, 100, 31, 48 (dark purple)
• CMYK 3, 68, 99, 0 (orange)
Should not have
• generic bbq branding

```html
<!DOCTYPE html>
<html lang="en">
<head>
<meta charset="utf-8">
<title>Willow Crest BBQ – Carolina Barbecue Sauce Label</title>
<link href="https://fonts.googleapis.com/css2?family=Oswald:wght@500;700&family=Roboto+Condensed:wght@400;700&family=Roboto+Slab:wght@800&display=swap" rel="stylesheet">
<style>
  :root {
    --orange: #f39a2e;
    --orange-deep: #e8861c;
    --purple: #2a1446;
    --white: #ffffff;
    --cream: #fff4e4;
  }
  html, body {
    margin: 0;
    padding: 0;
    width: 849px;
    height: 1200px;
    overflow: hidden;
    background: var(--orange);
  }
  .label {
    position: relative;
    width: 849px;
    height: 1200px;
    background: linear-gradient(90deg, var(--orange-deep) 0%, var(--orange) 22%, var(--orange) 78%, var(--orange-deep) 100%);
    display: flex;
    flex-direction: column;
    align-items: center;
    box-sizing: border-box;
    padding-top: 170px;
    color: var(--white);
    text-align: center;
  }
  .brand {
    display: flex;
    flex-direction: column;
    align-items: center;
    gap: 10px;
  }
  .brand-name {
    font-family: "Roboto Slab", serif;
    font-weight: 800;
    font-size: 74px;
    line-height: 0.95;
    color: var(--purple);
    letter-spacing: 1px;
  }
  .brand-place {
    font-family: "Roboto Condensed", sans-serif;
    font-size: 22px;
    font-style: normal;
    color: var(--white);
    letter-spacing: 1px;
  }
  .flavor {
    margin-top: 110px;
    font-family: "Oswald", sans-serif;
    font-weight: 700;
    font-size: 168px;
    line-height: 1;
    letter-spacing: 2px;
    text-transform: uppercase;
  }
  .flavor-note {
    margin-top: 34px;
    display: flex;
    align-items: center;
    gap: 18px;
    width: 440px;
  }
  .flavor-note .rule {
    flex: 1;
    height: 3px;
    background: var(--white);
  }
  .flavor-note span {
    font-family: "Oswald", sans-serif;
    font-weight: 500;
    font-size: 32px;
    letter-spacing: 5px;
    text-transform: uppercase;
    background: var(--cream);
    color: var(--orange-deep);
    padding: 2px 16px;
  }
  .product-type {
    margin-top: 24px;
    font-family: "Oswald", sans-serif;
    font-weight: 700;
    font-size: 52px;
    letter-spacing: 3px;
    text-transform: uppercase;
  }
  .description {
    margin-top: 28px;
    width: 520px;
    font-family: "Roboto Condensed", sans-serif;
    font-size: 20px;
    line-height: 1.4;
    text-transform: uppercase;
  }
  .net-contents {
    position: absolute;
    bottom: 190px;
    left: 0;
    right: 0;
    font-family: "Roboto Condensed", sans-serif;
    font-weight: 700;
    font-size: 22px;
    letter-spacing: 2px;
  }
</style>
</head>
<body>
  <main class="label">
    <header class="brand">
      <div class="brand-name">WILLOW CREST<br>BBQ</div>
      <div class="brand-place">Cedar Hollow, Texas</div>
    </header>

    <h1 class="flavor" style="margin-bottom:0;">Carolina</h1>

    <div class="flavor-note">
      <div class="rule"></div>
      <span>Mustard Based</span>
      <div class="rule"></div>
    </div>

    <div class="product-type">Barbecue Sauce</div>

    <p class="description">Slow simmered mustard sauce made in small batches with cider vinegar, brown sugar and cracked pepper for a tangy Carolina bite on pork, chicken and more.</p>

    <div class="net-contents">16 FL OZ / 473ML</div>
  </main>
</body>
</html>
```